Business Card Design Project

HI! Can you design a business card with the logo you designed for me? I don't know what the typical order is so can you place it in the order most people do? White background and also play with a couple of colored backgrounds. Thank you!

Darnette Ruval-Koskin
darnette@sunmorrowcoaching.com
sunmorrowcoaching.com
555-317-4082

Target Market(s)

Women

Industry/Entity Type

Business

```html
<!DOCTYPE html>
<html lang="en">
<head>
<meta charset="utf-8">
<title>Sunmorrow Coaching Services – Business Cards</title>
<link rel="stylesheet" href="https://fonts.googleapis.com/css2?family=Roboto:wght@400;700&family=Roboto+Condensed:wght@400;700&display=swap">
<style>
  :root {
    --stage: #2b2b2d;
    --paper: #ffffff;
    --paper-shade: #eeeeee;
    --brand-red: #b8182a;
    --brand-red-light: #d42a3c;
    --brand-red-dark: #961222;
    --brand-orange: #f6811c;
    --ink: #4a4a4a;
    --rule: #cfcfcf;
  }
  * { box-sizing: border-box; margin: 0; padding: 0; }
  html, body { width: 1200px; height: 900px; overflow: hidden; }
  body {
    background: var(--stage);
    font-family: "Roboto", Arial, sans-serif;
    display: flex;
    flex-direction: column;
    align-items: center;
    justify-content: center;
    gap: 60px;
  }
  .card {
    width: 630px;
    height: 360px;
    position: relative;
    overflow: hidden;
    box-shadow: 0 14px 30px rgba(0,0,0,0.45);
  }

  /* Contact side */
  .card--contact {
    background: linear-gradient(180deg, var(--paper) 0%, var(--paper-shade) 100%);
    display: flex;
  }
  .card--contact .brand-block {
    width: 52%;
    display: flex;
    flex-direction: column;
    align-items: center;
    justify-content: center;
    gap: 16px;
    padding-bottom: 24px;
  }
  .brand-mark {
    width: 58px;
    height: 58px;
    border-radius: 50%;
    background: var(--brand-orange);
  }
  .brand-name {
    font-family: "Roboto Condensed", Arial, sans-serif;
    font-weight: 700;
    font-size: 30px;
    line-height: 1.12;
    text-align: center;
    color: var(--brand-red);
  }
  .divider {
    width: 1px;
    background: var(--rule);
    margin: 58px 0 110px;
  }
  .contact-block {
    flex: 1;
    padding: 54px 0 0 26px;
  }
  .contact-name {
    font-family: "Roboto Condensed", Arial, sans-serif;
    font-weight: 700;
    font-size: 21px;
    color: var(--brand-red);
    margin-bottom: 18px;
  }
  .contact-list { list-style: none; }
  .contact-item {
    display: flex;
    align-items: center;
    gap: 10px;
    font-size: 13px;
    color: var(--ink);
    margin-bottom: 10px;
  }
  .contact-item--phone { font-size: 15px; }
  .contact-icon { width: 13px; height: 13px; flex: none; fill: var(--brand-red); }
  .edge-band {
    position: absolute;
    left: 0; right: 0; bottom: 0;
    height: 18px;
    background: var(--brand-red);
  }

  /* Brand side */
  .card--brand {
    background: radial-gradient(ellipse at 45% 35%, var(--brand-red-light) 0%, var(--brand-red) 55%, var(--brand-red-dark) 100%);
  }
  .card--brand .brand-block {
    position: absolute;
    left: 0; right: 0; top: 46px;
    display: flex;
    flex-direction: column;
    align-items: center;
    gap: 16px;
  }
  .card--brand .brand-mark {
    width: 72px;
    height: 72px;
    background: var(--paper);
  }
  .card--brand .brand-name {
    color: var(--paper);
    font-size: 36px;
  }
  .web-band {
    position: absolute;
    left: 0; right: 0; bottom: 0;
    height: 84px;
    background: var(--brand-orange);
    display: flex;
    align-items: center;
    justify-content: center;
  }
  .web-address {
    font-family: "Roboto Condensed", Arial, sans-serif;
    font-weight: 700;
    font-size: 19px;
    letter-spacing: 3px;
    color: var(--paper);
  }
</style>
</head>
<body>

  <section class="card card--contact">
    <div class="brand-block">
      <div class="brand-mark"></div>
      <p class="brand-name">Sunmorrow<br>Coaching Services</p>
    </div>
    <div class="divider"></div>
    <div class="contact-block">
      <h1 class="contact-name">Darnette Ruval-Koskin</h1>
      <ul class="contact-list">
        <li class="contact-item contact-item--phone">
          <svg class="contact-icon" viewBox="0 0 24 24" aria-hidden="true"><path d="M6.6 10.8a15.1 15.1 0 0 0 6.6 6.6l2.2-2.2a1 1 0 0 1 1-.25 11.4 11.4 0 0 0 3.6.57 1 1 0 0 1 1 1V20a1 1 0 0 1-1 1A17 17 0 0 1 3 4a1 1 0 0 1 1-1h3.5a1 1 0 0 1 1 1c0 1.25.2 2.45.57 3.6a1 1 0 0 1-.25 1z"/></svg>
          555-317-4082
        </li>
        <li class="contact-item">
          <svg class="contact-icon" viewBox="0 0 24 24" aria-hidden="true"><path d="M2 5h20v14H2z M4 7v.5l8 5 8-5V7z" fill-rule="evenodd"/></svg>
          darnette@sunmorrowcoaching.com
        </li>
        <li class="contact-item">
          <svg class="contact-icon" viewBox="0 0 24 24" aria-hidden="true"><path d="M12 2a10 10 0 1 0 0 20 10 10 0 0 0 0-20zm0 2c.9 0 2.2 1.9 2.7 5H9.3C9.8 5.9 11.1 4 12 4zM4.3 11h3a16 16 0 0 0 0 2h-3a8 8 0 0 1 0-2zm5 0h5.4a14 14 0 0 1 0 2H9.3a14 14 0 0 1 0-2zm7.4 0h3a8 8 0 0 1 0 2h-3a16 16 0 0 0 0-2zM12 20c-.9 0-2.2-1.9-2.7-5h5.4c-.5 3.1-1.8 5-2.7 5z"/></svg>
          www.sunmorrowcoaching.com
        </li>
      </ul>
    </div>
    <div class="edge-band"></div>
  </section>

  <section class="card card--brand">
    <div class="brand-block">
      <div class="brand-mark"></div>
      <p class="brand-name">Sunmorrow<br>Coaching Services</p>
    </div>
    <div class="web-band">
      <p class="web-address">WWW.SUNMORROWCOACHING.COM</p>
    </div>
  </section>

</body>
</html>
```